International oil and gas consultancy business needs a web design

Hello, I need a web design for a new oil and gas auditing consultancy business. My business undertakes contract audit assignments to review past costs of oil and gas operations (see attached Excel file for more details of the businesses services). I need the design to give the impression of a professional consultancy style of business, rather than a retail style of website. Note: this job is for LAYOUT DESIGN ONLY and not coding / development work.
The following are my key design principles:
1. BASIC DESIGN: I am after a simple and static web design. I don't want the pages busy or cluttered with too many images or detail.
2. HORIZONTAL TABS: I require a horizontal set of tabs towards the top of the screens (see Excel file) which remain in the same position on every page.
3. META TAG PLANNING: The design should allow for effective positioning of content so that key meta tag words can easily be built during the technical build stage.
4. NUMBER OF PAGES: The site will eventually have a maximum of 10 pages. Seven of the pages will reside under the tabs. Can you please present your opening submission for the first two page.
5. USE OF MY LOGO: The attached logo (JPEG file) should be used throughout the website. Please don't change the shape and colour.
6. COLOUR SCHEMES: Can you please consider any of the 3 colour schemes below:
A - dark red (to match the logo), light grey and perhaps another of your liking;
B - dark red (to match the logo), light cream and perhaps another of your liking;
C - dark red (to match the logo), white and perhaps another of your liking.
7. WORD CONTENT: I have attached an Excel file which shows the estimated word content for each page.
8. FUTURE USE OF DESIGN: I'm planning on building a Wordpress website. Can you please ensure the layout design supports this application.

Target Market(s)

oil and gas companies (small and large)

Industry/Entity Type

Oil And Gas

Font styles to use
Sans Serif

Requirements
Nice to have
• The KOL logo and business name should ideally be next to each other. Also, the logo and name should be part of the background graphics, not above it.

```html
<!DOCTYPE html>
<html lang="en">
<head>
<meta charset="utf-8">
<title>Kestrel Oilfield Auditing</title>
<link href="https://fonts.googleapis.com/css2?family=Open+Sans:ital,wght@0,400;0,600;0,700;1,700&family=Arimo:ital,wght@0,400;1,700&display=swap" rel="stylesheet">
<style>
  :root {
    --brand-red: #9b1b1e;
    --band-red: #a01a1d;
    --charcoal: #3d3d3d;
    --ink: #333333;
    --body-text: #555555;
    --rule: #d6d6d6;
    --white: #ffffff;
  }
  * { margin: 0; padding: 0; box-sizing: border-box; }
  html, body { width: 1200px; height: 1002px; overflow: hidden; background: var(--white); }
  body { position: relative; font-family: "Open Sans", Arial, sans-serif; color: var(--ink); }

  .brand { position: absolute; left: 183px; top: 22px; color: var(--brand-red); }
  .brand-mark { display: block; width: 241px; text-align: center; font-size: 26px; font-weight: 700; letter-spacing: 2px; line-height: 30px; }
  .brand-name { display: block; font-size: 24px; font-weight: 400; line-height: 30px; }
  .brand-divider { position: absolute; left: 470px; top: 34px; width: 1px; height: 43px; background: var(--brand-red); }
  .brand-region { position: absolute; left: 482px; top: 45px; font-size: 15px; color: var(--brand-red); }

  .search { position: absolute; left: 866px; top: 43px; width: 152px; height: 24px; border: 1px solid var(--rule); display: flex; align-items: center; }
  .search-field { flex: 1; padding-left: 7px; font-size: 9px; font-style: italic; color: #666; }
  .search-button { width: 18px; height: 18px; margin-right: 2px; background: var(--charcoal); display: flex; align-items: center; justify-content: center; }

  .main-nav { position: absolute; left: 183px; top: 106px; width: 835px; height: 39px; background: var(--charcoal); display: flex; }
  .main-nav a { position: relative; color: var(--white); text-decoration: none; font-size: 12px; line-height: 39px; padding: 0 15.5px; text-transform: uppercase; }
  .main-nav a::after { content: ""; position: absolute; right: 0; top: 12px; width: 1px; height: 15px; background: #8a8a8a; }
  .main-nav a.is-active { background: var(--band-red); padding: 0 15px 0 24px; }
  .main-nav a.is-active::after { display: none; }

  .hero { position: absolute; left: 183px; top: 145px; width: 835px; height: 245px; overflow: hidden;
    background: linear-gradient(180deg, #e7b38c 0%, #b7a59c 22%, #4f6486 45%, #3b5478 70%, #2e4466 100%); }
  .hero-photo { position: absolute; inset: 0; }
  .hero-copy { position: absolute; left: 41px; top: 112px; color: var(--white); font-family: Arimo, Arial, sans-serif; font-weight: 700; }
  .hero-title { font-size: 35px; letter-spacing: -1.5px; line-height: 40px; }
  .hero-list { list-style: none; margin-top: 2px; font-size: 18px; letter-spacing: -0.5px; line-height: 23px; }

  .intro { position: absolute; left: 197px; top: 416px; width: 810px; }
  .section-title { font-size: 21.5px; font-weight: 400; color: var(--ink); line-height: 30px; }
  .intro p { margin-top: 9px; font-family: Arimo, Arial, sans-serif; font-size: 10px; line-height: 18.5px; color: var(--ink); }
  .services-title { position: absolute; left: 197px; top: 522px; }

  .service-card { position: absolute; top: 570px; width: 239px; height: 242px; border: 1px solid var(--rule); background: var(--white); }
  .service-card::after { content: ""; position: absolute; left: 12px; right: 12px; bottom: -8px; height: 8px; border-radius: 50%;
    background: radial-gradient(ellipse at center top, rgba(0,0,0,0.35), rgba(0,0,0,0) 70%); }
  .service-photo { height: 124px; }
  .service-band { height: 30px; background: var(--band-red); color: var(--white); font-size: 22px; font-weight: 700; text-align: center; line-height: 30px; }
  .service-card p { padding: 11px 12px 0 14px; font-family: Arimo, Arial, sans-serif; font-size: 9.6px; line-height: 15.4px; color: var(--body-text); }
  .card-joint { left: 197px; }
  .card-contract { left: 481px; }
  .card-operations { left: 765px; }
  .photo-signing { background: linear-gradient(160deg, #dfe6f2 0%, #9fb2d3 55%, #3e62a8 100%); }
  .photo-meeting { background: linear-gradient(180deg, #f4f4f4 0%, #9a9a9a 60%, #2b2d33 100%); }
  .photo-site { background: linear-gradient(180deg, #f6f6f6 0%, #d8dce6 50%, #3a3c44 100%); }

  .site-footer { position: absolute; left: 0; top: 874px; width: 1200px; height: 128px; background: var(--charcoal); color: var(--white); font-family: Arimo, Arial, sans-serif; text-align: center; }
  .footer-nav { margin-top: 19px; font-size: 10.5px; }
  .footer-nav a { color: var(--white); text-decoration: none; }
  .footer-nav .sep { margin: 0 14px; }
  .copyright { margin-top: 15px; font-size: 10px; }
  .credit { margin-top: 11px; font-size: 10px; }
  .credit strong { font-style: italic; font-weight: 700; }
</style>
</head>
<body>
  <header>
    <div class="brand">
      <span class="brand-mark">KOL</span>
      <span class="brand-name">Kestrel Oilfield Auditing</span>
    </div>
    <div class="brand-divider"></div>
    <div class="brand-region">Australia</div>

    <div class="search">
      <span class="search-field">Search</span>
      <span class="search-button">
        <svg width="11" height="11" viewBox="0 0 11 11"><circle cx="4.5" cy="4.5" r="3.3" fill="none" stroke="#fff" stroke-width="1.4"/><line x1="7" y1="7" x2="10" y2="10" stroke="#fff" stroke-width="1.6"/></svg>
      </span>
    </div>

    <nav class="main-nav">
      <a href="#" class="is-active">Home</a>
      <a href="#">About Us</a>
      <a href="#">Services</a>
      <a href="#">Our Partners</a>
      <a href="#">Approach</a>
      <a href="#">Why Choose Us</a>
      <a href="#">Contact Us</a>
    </nav>
  </header>

  <section class="hero">
    <div class="hero-photo" role="img" aria-label="Red suspension bridge spanning a blue bay at sunset with a city skyline behind"></div>
    <div class="hero-copy">
      <h1 class="hero-title">Our Approach</h1>
      <ul class="hero-list">
        <li>Planning</li>
        <li>Field Work</li>
        <li>Completion</li>
      </ul>
    </div>
  </section>

  <section class="intro">
    <h2 class="section-title">Welcome to Kestrel Oilfield Auditing.</h2>
    <p>Kestrel Oilfield Auditing is a Perth (Australia) based firm specialising in providing quality audit services for the oil and gas industry. Our skills and knowledge of oil and gas, along with a deep understanding of business commercial needs, ensures the high quality of our services</p>
  </section>

  <h2 class="section-title services-title">Kestrel Oilfield Auditing specialise in the following services:</h2>

  <article class="service-card card-joint">
    <div class="service-photo photo-signing" role="img" aria-label="Blue pen resting on a signed agreement"></div>
    <h3 class="service-band">Joint Venture Audits</h3>
    <p>Lorem Ipsum has been the industry's standard dummy text ever since the 1500s, when an unknown printer took a galley of type and scrambled it to make a type specimen book.</p>
  </article>

  <article class="service-card card-contract">
    <div class="service-photo photo-meeting" role="img" aria-label="Two businessmen in suits reviewing documents"></div>
    <h3 class="service-band">Contract Audits</h3>
    <p>Lorem Ipsum has been the industry's standard dummy text ever since the 1500s, when an unknown printer took a galley of type and scrambled it to make a type specimen book.</p>
  </article>

  <article class="service-card card-operations">
    <div class="service-photo photo-site" role="img" aria-label="Two engineers in hard hats discussing plans"></div>
    <h3 class="service-band">Operations Audits</h3>
    <p>Lorem Ipsum has been the industry's standard dummy text ever since the 1500s, when an unknown printer took a galley of type and scrambled it to make a type specimen book.</p>
  </article>

  <footer class="site-footer">
    <nav class="footer-nav">
      <a href="#">Home</a><span class="sep">I</span><a href="#">About Us</a><span class="sep">I</span><a href="#">Services</a><span class="sep">I</span><a href="#">Our Partners</a><span class="sep">I</span><a href="#">Approach</a><span class="sep">I</span><a href="#">Why Choose us</a><span class="sep">I</span><a href="#">Contact us</a>
    </nav>
    <p class="copyright">© 2014 Ember Sky. All rights reserved.</p>
    <p class="credit">Designed by <strong>Bright Frame Studio</strong></p>
  </footer>
</body>
</html>
```